Design a box for EV Charging Cables - Electric Cars

https://files.plumworks.example/sheet/q7Rz2mXv9LpT4nWc8BsYd3KfHj6GaE1u/view?mode=shared

We are looking to design a box to package our EV charging cables. This box needs to be 40cm x 40cm x 11cm.

It needs to include:
- Our logo
- Images of our products
- Accreditations

My websites are:
https://voltharbor.co.uk/
https://www.plugwiremart.co.uk/
https://www.zap-drive.co.uk/

Logo:
https://picdrop.example/K8tnw2P
https://picdrop.example/hRzQLdu
https://picdrop.example/vyNkC7j
https://picdrop.example/92bqzrf

Rather than having a list of products. I would like to have tick boxes:
1st tick box: Connector Type From: (Type 2, 3 Pin),
2nd tick box: Connector Type To: (Type 1, Type 2),
3rd tick box: Amp/Charge Speed (13amp/16amp/32amp/32amp - 3 Phase)
4th tick box: Length (5m/10m/15m)

Target Market(s)

People who own electric cars

Industry/Entity Type

Automotive

Colors

Designer to choose colors to be used in the design.

Requirements
Must have
• Our colours, logo, list of products we sell
Nice to have
• Rather than having a list of products. I would like to have tick boxes: 1st tick box should be: Connector Type From: (Type 2, 3 Pin), Connector Type To: (Type 1, Type 2), Third: Amp/Charge Speed (13amp/16amp/32amp/32amp - 3 Phase) Third: Length (5m/10m/15m)
Should not have
• Transparent Section

```html
<!DOCTYPE html>
<html lang="en">
<head>
<meta charset="utf-8">
<title>Zap Drive – EV Charging Cables Box</title>
<link rel="stylesheet" href="https://fonts.googleapis.com/css2?family=Chakra+Petch:ital,wght@0,400;0,600;0,700;1,700&display=swap">
<style>
  :root{
    --green:#6cbd2d;
    --green-deep:#55a31f;
    --lime:#c5df6a;
    --dark:#2a2c29;
    --card:rgba(40,42,38,.9);
    --white:#ffffff;
    --paper:#f1f2ef;
    --orange:#ee6a1f;
    --ink:#333;
    --font:"Chakra Petch", sans-serif;
  }
  *{box-sizing:border-box;margin:0;padding:0}
  html,body{width:1200px;height:2740px;overflow:hidden}
  body{background:var(--paper);font-family:var(--font);color:var(--ink);position:relative}

  .panel{position:absolute;left:100px;width:1000px;background:var(--white);overflow:hidden;box-shadow:0 6px 24px rgba(0,0,0,.08)}
  .front{top:90px;height:1000px}
  .back{top:1170px;height:1000px}
  .spine{top:2250px;height:275px;display:flex}

  .brand{position:absolute;display:flex;align-items:center;gap:14px;color:var(--green);font-weight:700;letter-spacing:.06em;text-transform:uppercase;font-family:var(--font)}
  .brand .dot{width:26px;height:26px;border-radius:50%;background:var(--green)}
  .seal{position:absolute;border-radius:50%;background:radial-gradient(circle,#d9d9d9,#8f8f8f)}

  /* front */
  .front .brand{left:70px;top:180px;font-size:64px}
  .front .seal{right:70px;top:60px;width:150px;height:150px}
  .front-field{position:absolute;left:0;top:340px;width:1000px;height:660px;background:linear-gradient(160deg,var(--green),var(--green-deep));border-top-right-radius:70px}
  .title-tag{position:absolute;left:60px;top:380px;width:430px;height:110px;background:var(--lime);border-radius:14px 14px 0 0;display:flex;align-items:center;justify-content:center;text-align:center;font-style:italic;font-weight:700;font-size:40px;line-height:1;color:var(--dark)}
  .spec-card{position:absolute;left:60px;top:490px;width:430px;height:470px;background:var(--card);border-radius:0 0 14px 14px;padding:24px 28px;color:var(--white)}
  .spec-card .headline{font-size:40px;font-weight:700;color:var(--lime);border-bottom:2px solid rgba(255,255,255,.8);padding-bottom:10px}
  .spec-card .headline span{font-size:24px;color:var(--white);font-weight:600}
  .ticks{list-style:none}
  .ticks li{display:flex;gap:12px;align-items:flex-start;font-size:19px;line-height:1.25;padding:12px 0;border-bottom:2px solid rgba(255,255,255,.8)}
  .ticks svg{flex:none;margin-top:6px}
  .warranty{display:flex;align-items:center;gap:14px;margin-top:22px}
  .warranty .shield{width:54px;height:62px}
  .warranty .bar{flex:1;border:2px solid var(--white);border-radius:6px;padding:6px 12px;font-size:18px;font-weight:600}
  .product-art{position:absolute;left:530px;top:380px;width:420px;height:460px;border-radius:20px;background:linear-gradient(160deg,#2c2f2a,#4b8e25)}
  .level-tag{position:absolute;right:60px;top:870px;background:var(--dark);color:var(--white);font-size:28px;font-weight:600;padding:8px 18px;border-radius:4px}

  /* back */
  .back .brand{left:60px;top:70px;font-size:56px}
  .back .seal{right:70px;top:60px;width:120px;height:120px}
  .back-copy{position:absolute;left:60px;top:200px;width:470px;font-size:18px;line-height:1.4;text-align:justify;color:var(--dark)}
  .features{position:absolute;left:60px;top:420px;width:470px;list-style:none}
  .features li{display:flex;align-items:center;gap:18px;font-size:20px;font-weight:600;padding:10px 0;color:var(--dark)}
  .features .icon{width:46px;height:46px;border-radius:8px;background:var(--dark);display:flex;align-items:center;justify-content:center}
  .maker-band{position:absolute;left:0;top:700px;width:1000px;height:300px;background:linear-gradient(160deg,var(--green),var(--green-deep));border-top-right-radius:60px;padding:26px 60px;color:var(--white);font-size:22px;font-weight:600}
  .back-art{position:absolute;left:570px;top:200px;width:370px;height:440px;border-radius:20px;background:linear-gradient(160deg,#2b2d2a,#555,#4b8e25)}
  .promo{position:absolute;left:570px;top:740px;width:370px;display:flex;flex-direction:column;gap:6px}
  .promo div{color:var(--white);padding:10px 14px;font-weight:700;font-size:18px;line-height:1.15}
  .promo small{display:block;font-weight:400;font-size:12px}
  .promo .orange{background:var(--orange)}
  .promo .dark{background:var(--dark)}
  .promo .green{background:var(--green-deep);border:2px solid var(--white)}

  /* spine */
  .spine .top{position:absolute;left:0;top:0;width:1000px;height:120px;background:var(--white)}
  .spine .bottom{position:absolute;left:0;top:120px;width:1000px;height:155px;background:linear-gradient(160deg,var(--green),var(--green-deep))}
  .spine .brand{left:60px;top:34px;font-size:44px}
</style>
</head>
<body>

<section class="panel front" aria-label="Box front">
  <div class="brand"><span class="dot"></span>Zap Drive</div>
  <div class="seal" role="img" aria-label="Premium quality seal"></div>
  <div class="front-field"></div>
  <div class="title-tag">EV CHARGING<br>CABLES</div>
  <div class="spec-card">
    <p class="headline">2,500 <span>VDC Tested</span></p>
    <ul class="ticks">
      <li><svg width="18" height="18" viewBox="0 0 18 18"><rect x="1" y="1" width="16" height="16" fill="none" stroke="#c5df6a" stroke-width="2"/><path d="M4 9l3 3 7-7" fill="none" stroke="#c5df6a" stroke-width="2.4"/></svg>Connector Type From:<br>(Type 2, 3 Pin)</li>
      <li><svg width="18" height="18" viewBox="0 0 18 18"><rect x="1" y="1" width="16" height="16" fill="none" stroke="#c5df6a" stroke-width="2"/><path d="M4 9l3 3 7-7" fill="none" stroke="#c5df6a" stroke-width="2.4"/></svg>Connector Type To:<br>(Type 1, Type 2)</li>
      <li><svg width="18" height="18" viewBox="0 0 18 18"><rect x="1" y="1" width="16" height="16" fill="none" stroke="#c5df6a" stroke-width="2"/><path d="M4 9l3 3 7-7" fill="none" stroke="#c5df6a" stroke-width="2.4"/></svg>Amp/Charge Speed (13amp/<br>16amp/32amp/32amp-3 Phase)</li>
      <li><svg width="18" height="18" viewBox="0 0 18 18"><rect x="1" y="1" width="16" height="16" fill="none" stroke="#c5df6a" stroke-width="2"/><path d="M4 9l3 3 7-7" fill="none" stroke="#c5df6a" stroke-width="2.4"/></svg>Length (5m/10m/15m)</li>
    </ul>
    <div class="warranty">
      <svg class="shield" viewBox="0 0 54 62"><path d="M27 2L51 10v20c0 16-11 26-24 30C14 56 3 46 3 30V10z" fill="none" stroke="#fff" stroke-width="3"/><text x="27" y="40" text-anchor="middle" fill="#fff" font-family="Chakra Petch, sans-serif" font-weight="700" font-size="22">18</text></svg>
      <div class="bar">MONTHS WARRANTY</div>
    </div>
  </div>
  <div class="product-art" role="img" aria-label="Product photo: Type 2 connector, 3-pin plug and control box on charging cable"></div>
  <div class="level-tag">10A LAVEL 2</div>
</section>

<section class="panel back" aria-label="Box back">
  <div class="brand"><span class="dot"></span>Zap Drive</div>
  <div class="seal" role="img" aria-label="Premium quality seal"></div>
  <p class="back-copy">Having the correct EV Charging equipment is crucial to owning an Electric Car. Pulling up at a local EV charger without the proper equipment can be frustrating. Here at Volt Harbor, we provide all types of electric car charging cables to make sure you can always charge your electric vehicle no matter the situation.</p>
  <ul class="features">
    <li><span class="icon"><svg width="24" height="24" viewBox="0 0 24 24"><path d="M12 3c4 5 6 8 6 11a6 6 0 0 1-12 0c0-3 2-6 6-11z" fill="#6cbd2d"/></svg></span>Over heating Protection</li>
    <li><span class="icon"><svg width="24" height="24" viewBox="0 0 24 24"><rect x="4" y="6" width="16" height="12" rx="2" fill="#6cbd2d"/></svg></span>Over current Protection</li>
    <li><span class="icon"><svg width="24" height="24" viewBox="0 0 24 24"><path d="M13 2L5 14h6l-1 8 8-12h-6z" fill="#6cbd2d"/></svg></span>Over voltage Protection</li>
    <li><span class="icon"><svg width="24" height="24" viewBox="0 0 24 24"><path d="M12 4c3 4 5 7 5 10a5 5 0 0 1-10 0c0-3 2-6 5-10z" fill="none" stroke="#6cbd2d" stroke-width="2.5"/></svg></span>Leakage Protection</li>
  </ul>
  <div class="maker-band">Manufacture by: Zap Drive</div>
  <div class="back-art" role="img" aria-label="Product photos: Type 2 socket face, 3-pin plug and coiled charging cable"></div>
  <div class="promo">
    <div class="orange">FREE DELIVERY AS STANDARD<small>On all UK orders</small></div>
    <div class="dark">3 YEARS GUARANTEE<small>On every cable</small></div>
    <div class="green">PRICE MATCH GUARANTEE<small>Found it cheaper? Ask us</small></div>
  </div>
</section>

<section class="panel spine" aria-label="Box side">
  <div class="top"></div>
  <div class="bottom"></div>
  <div class="brand"><span class="dot"></span>Zap Drive</div>
</section>

</body>
</html>
```